Design a sharp Business Card, Stationary, and PowerPoint Template for Harbor Lantern Group (HLG)
Harbor Lantern Group (HLG) is a consulting firm with a mission
Professional
Maren Coleby Ashdown
Managing Director
4870 Larkspur Blvd. NW
Suite 2300
Washington, DC 20417
maren@harborlntn.example
www.harborlntn.example
I'm looking for something sharp that incorporates the colors of the logo.
Business card designs (only), please include this text:
We work with the military, private sector, and nonprofits to protect people affected by conflict and disaster.
This is the logo for Harbor Lantern Group (HLG). The black and red color combo is preferred.
For design purposes, the symbol can be used separately from the text and watermarked.

```html
<!DOCTYPE html>
<html lang="en">
<head>
<meta charset="utf-8">
<title>Harbor Lantern Group – Business Card</title>
<link rel="stylesheet" href="https://fonts.googleapis.com/css2?family=Open+Sans:ital,wght@0,300;0,400;0,600;1,400;1,600&display=swap">
<style>
  :root {
    --charcoal: #2e2e30;
    --brand-red: #d8262b;
    --paper: #ffffff;
    --ink: #3a3a3c;
    --rule-grey: #c9c9c9;
    --backdrop: #e9e7e4;
    --light-text: #f1f1f1;
  }
  * { margin: 0; padding: 0; box-sizing: border-box; }
  html, body {
    width: 1200px; height: 914px; overflow: hidden;
    background: var(--backdrop);
    font-family: "Open Sans", Arial, sans-serif;
  }
  .canvas { position: relative; width: 1200px; height: 914px; }
  .business-card {
    position: absolute; left: 100px; top: 171px;
    width: 1000px; height: 572px;
    background: var(--paper);
    box-shadow: 0 18px 40px rgba(0,0,0,0.18);
    overflow: hidden;
  }
  .card-shape { position: absolute; inset: 0; }
  .holder { position: absolute; left: 60px; top: 38px; }
  .holder-name {
    color: var(--brand-red); font-size: 26px; font-weight: 600; font-style: italic;
  }
  .holder-title {
    color: var(--light-text); font-size: 21px; font-style: italic; margin-top: 2px;
  }
  .contact { position: absolute; left: 60px; top: 268px; color: var(--light-text); font-size: 19px; line-height: 1.45; }
  .contact-address { margin-bottom: 6px; }
  .contact-line { display: flex; align-items: center; gap: 10px; }
  .contact-icon { width: 20px; height: 20px; flex: none; }
  .brand { position: absolute; left: 628px; top: 196px; display: flex; align-items: center; gap: 26px; }
  .brand-dot { width: 86px; height: 86px; border-radius: 50%; background: var(--brand-red); flex: none; }
  .brand-name {
    color: var(--ink); font-size: 40px; font-weight: 300; letter-spacing: 6px;
    line-height: 1.12; text-transform: uppercase;
  }
</style>
</head>
<body>
<div class="canvas">
  <div class="business-card">
    <svg class="card-shape" viewBox="0 0 1000 572" width="1000" height="572" aria-hidden="true">
      <path d="M0 0 H560 C660 170 610 430 430 572 H0 Z" fill="var(--charcoal)"/>
      <path d="M566 -4 C668 170 618 432 438 576" fill="none" stroke="var(--brand-red)" stroke-width="11"/>
      <path d="M586 -4 C688 172 636 434 458 576" fill="none" stroke="var(--rule-grey)" stroke-width="2"/>
    </svg>

    <div class="holder">
      <p class="holder-name">Maren Coleby Ashdown</p>
      <p class="holder-title">Managing Director</p>
    </div>

    <div class="contact">
      <p class="contact-address">4870 Larkspur Blvd. NW<br>Suite 2300 Washington, DC 20417</p>
      <p class="contact-line">
        <svg class="contact-icon" viewBox="0 0 20 20" aria-hidden="true"><circle cx="10" cy="10" r="10" fill="var(--brand-red)"/><path d="M6.5 5.5l2 .3.6 2.3-1.2 1a6 6 0 0 0 3 3l1-1.2 2.3.6.3 2c-4.5.6-8.6-3.5-8-8z" fill="#fff"/></svg>
        202-555-0143</p>
      <p class="contact-line">
        <svg class="contact-icon" viewBox="0 0 20 20" aria-hidden="true"><circle cx="10" cy="10" r="10" fill="var(--brand-red)"/><path d="M6.5 5.5l2 .3.6 2.3-1.2 1a6 6 0 0 0 3 3l1-1.2 2.3.6.3 2c-4.5.6-8.6-3.5-8-8z" fill="#fff"/></svg>
        202-555-0186</p>
      <p class="contact-line">
        <svg class="contact-icon" viewBox="0 0 20 20" aria-hidden="true"><circle cx="10" cy="10" r="10" fill="var(--brand-red)"/><rect x="5" y="6.5" width="10" height="7" fill="none" stroke="#fff" stroke-width="1.3"/><path d="M5 6.8l5 4 5-4" fill="none" stroke="#fff" stroke-width="1.3"/></svg>
        maren@harborlntn.example</p>
      <p class="contact-line">
        <svg class="contact-icon" viewBox="0 0 20 20" aria-hidden="true"><circle cx="10" cy="10" r="10" fill="var(--brand-red)"/><circle cx="10" cy="10" r="5" fill="none" stroke="#fff" stroke-width="1.2"/><path d="M5 10h10M10 5c-2.5 3-2.5 7 0 10M10 5c2.5 3 2.5 7 0 10" fill="none" stroke="#fff" stroke-width="1"/></svg>
        www.harborlntn.example</p>
    </div>

    <div class="brand">
      <span class="brand-dot"></span>
      <p class="brand-name">Harbor<br>Lantern<br>Group</p>
    </div>
  </div>
</div>
</body>
</html>
```